BRIGHTDOOR7 - business card, letterhead and envelopes
BRIGHTDOOR7 - Business cards, letterhead and envelopes
Professional
BRIGHTDOOR7 LLC
Real Estate Solution Provider
info@brightdoor7.example
www.brightdoor7.example
We specialize in creative real estate solutions
We pay cash for houses!
We prevent foreclosures !
We help repair credit!
We pay referral fees!

```html
<!DOCTYPE html>
<html lang="en">
<head>
<meta charset="utf-8">
<title>BRIGHTDOOR7 Stationery Set</title>
<link href="https://fonts.googleapis.com/css2?family=Arimo:wght@400;700&display=swap" rel="stylesheet">
<style>
  :root {
    --ink: #0c0c0e;
    --paper: #ffffff;
    --canvas: #ffffff;
    --gold: #e3b84a;
    --blue: #5a7fc0;
    --rule: #d6d6d6;
    --text: #3a3a3a;
    --muted: #9a9a9a;
    --light: #e8e8e8;
  }
  * { box-sizing: border-box; margin: 0; padding: 0; }
  html, body { width: 1200px; height: 482px; overflow: hidden; background: var(--canvas); }
  body { position: relative; font-family: "Arimo", Arial, sans-serif; color: var(--text); }

  .frame-rule { position: absolute; left: 14px; right: 14px; height: 1px; background: var(--light); }
  .frame-rule.top { top: 12px; }
  .frame-rule.bottom { bottom: 14px; }

  .sheet { position: absolute; background: var(--paper); border: 1px solid var(--rule); box-shadow: 0 1px 3px rgba(0,0,0,.12); }
  .header-band { position: absolute; left: 0; right: 0; top: 0; background: var(--ink); }
  .header-band::after { content: ""; position: absolute; left: 0; right: 0; bottom: -3px; height: 3px;
    background: linear-gradient(90deg, var(--blue) 0 50%, var(--gold) 50% 100%); }

  .brand { position: absolute; display: flex; align-items: center; gap: 4px;
    color: var(--gold); font-weight: 700; letter-spacing: .5px; white-space: nowrap; }
  .brand .mark { display: block; width: 6px; height: 6px; background: var(--gold); }

  .contact { position: absolute; color: #cfcfcf; font-size: 5px; line-height: 7px; text-align: left; white-space: nowrap; }

  /* fax cover sheet */
  .fax { left: 43px; top: 34px; width: 280px; height: 405px; }
  .fax .header-band { height: 56px; }
  .fax .brand { left: 14px; top: 30px; font-size: 11px; }
  .fax .contact { left: 188px; top: 8px; }
  .fax-fields { position: absolute; left: 16px; top: 168px; width: 250px;
    display: grid; grid-template-columns: 1fr 1fr; column-gap: 24px; row-gap: 9px; }
  .field { display: flex; align-items: flex-end; gap: 6px; font-size: 5.5px; color: var(--text); }
  .field .line { flex: 1; height: 1px; background: #b5b5b5; }
  .field .label { width: 20px; }
  .fax-options { position: absolute; left: 16px; top: 245px; display: flex; gap: 12px; font-size: 5px; }
  .option { display: flex; align-items: center; gap: 3px; }
  .option .box { width: 5px; height: 5px; border: 1px solid #777; }

  /* envelope front */
  .envelope-front { left: 396px; top: 72px; width: 324px; height: 173px; }
  .envelope-front .header-band { height: 52px; }
  .envelope-front .brand { left: 14px; top: 26px; font-size: 11px; }
  .envelope-front .contact { left: 222px; top: 8px; }

  /* envelope back */
  .envelope-back { left: 396px; top: 281px; width: 324px; height: 163px; }
  .envelope-back svg { position: absolute; left: 0; top: 0; }
  .envelope-back .brand { left: 50%; top: 36px; transform: translateX(-50%); font-size: 10px; color: var(--ink); }
  .envelope-back .brand .mark { background: var(--ink); }

  /* letterhead */
  .letterhead { left: 780px; top: 34px; width: 264px; height: 405px; }
  .letterhead .header-band { height: 56px; }
  .letterhead .brand { left: 12px; top: 30px; font-size: 10.5px; }
  .letterhead .contact { left: 176px; top: 8px; }

  /* business cards */
  .card { position: absolute; left: 1068px; width: 108px; height: 72px; background: var(--ink);
    box-shadow: 0 1px 3px rgba(0,0,0,.25); color: #d8d8d8; overflow: hidden; }
  .card-front { top: 120px; }
  .card-back { top: 204px; }
  .card-front .brand { left: 5px; top: 33px; font-size: 5.5px; gap: 3px; letter-spacing: .3px; }
  .card-front .brand .mark { width: 4px; height: 4px; }
  .card-front .holder { position: absolute; left: 60px; top: 10px; font-size: 3.6px; line-height: 5.5px; white-space: nowrap; }
  .card-front .holder strong { color: var(--gold); font-size: 4.5px; }
  .card-back .company { position: absolute; left: 0; right: 0; top: 24px; text-align: center;
    font-size: 5.5px; color: var(--gold); font-weight: 700; }
  .card-back .tagline { position: absolute; left: 0; right: 0; top: 34px; text-align: center; font-size: 4.5px; }
  .card-back .rule { position: absolute; left: 24px; right: 24px; top: 31px; height: 1px; background: var(--blue); }
</style>
</head>
<body>
  <div class="frame-rule top"></div>
  <div class="frame-rule bottom"></div>

  <section class="sheet fax" aria-label="Fax cover sheet">
    <div class="header-band">
      <div class="brand"><span class="mark"></span>BRIGHTDOOR7</div>
      <div class="contact">PO Box 4410<br>Phone 555 0142<br>Fax 555 0143<br>info@brightdoor7.example<br>www.brightdoor7.example</div>
    </div>
    <div class="fax-fields">
      <div class="field"><span class="label">To:</span><span class="line"></span></div>
      <div class="field"><span class="label">From:</span><span class="line"></span></div>
      <div class="field"><span class="label">Fax:</span><span class="line"></span></div>
      <div class="field"><span class="label">Pages:</span><span class="line"></span></div>
      <div class="field"><span class="label">Phone:</span><span class="line"></span></div>
      <div class="field"><span class="label">Date:</span><span class="line"></span></div>
      <div class="field"><span class="label">Re:</span><span class="line"></span></div>
      <div class="field"><span class="label">CC:</span><span class="line"></span></div>
    </div>
    <div class="fax-options">
      <span class="option"><span class="box"></span>Urgent</span>
      <span class="option"><span class="box"></span>For Review</span>
      <span class="option"><span class="box"></span>Please Comment</span>
      <span class="option"><span class="box"></span>Please Reply</span>
      <span class="option"><span class="box"></span>Please Recycle</span>
    </div>
  </section>

  <section class="sheet envelope-front" aria-label="Envelope front">
    <div class="header-band">
      <div class="brand"><span class="mark"></span>BRIGHTDOOR7</div>
      <div class="contact">PO Box 4410<br>Phone 555 0142<br>Fax 555 0143<br>info@brightdoor7.example<br>www.brightdoor7.example</div>
    </div>
  </section>

  <section class="sheet envelope-back" aria-label="Envelope back">
    <svg width="324" height="163" viewBox="0 0 324 163" aria-hidden="true">
      <polyline points="0,0 162,62 324,0" fill="none" stroke="#c8c8c8" stroke-width="1"/>
      <polyline points="0,163 140,80" fill="none" stroke="#e0e0e0" stroke-width="1"/>
      <polyline points="324,163 184,80" fill="none" stroke="#e0e0e0" stroke-width="1"/>
    </svg>
    <div class="brand"><span class="mark"></span>BRIGHTDOOR7</div>
  </section>

  <section class="sheet letterhead" aria-label="Letterhead">
    <div class="header-band">
      <div class="brand"><span class="mark"></span>BRIGHTDOOR7</div>
      <div class="contact">PO Box 4410<br>Phone 555 0142<br>Fax 555 0143<br>info@brightdoor7.example<br>www.brightdoor7.example</div>
    </div>
  </section>

  <section class="card card-front" aria-label="Business card front">
    <div class="brand"><span class="mark"></span>BRIGHTDOOR7</div>
    <div class="holder"><strong>Dana Reyes</strong><br>Acquisitions Lead<br>Phone 555 0142<br>info@brightdoor7.example</div>
  </section>

  <section class="card card-back" aria-label="Business card back">
    <div class="company">BRIGHTDOOR7 LLC</div>
    <div class="rule"></div>
    <div class="tagline">Real Estate Solution Provider</div>
  </section>
</body>
</html>
```